Physiotherapy Referral Pad

-Need a referral pad for physiotherapy to be provided to doctors' offices. I would like it to be simple, not too cluttered and sharp looking so doctors can quickly complete it for clients.

-I have attached my logo which I would like to include. I have also included my business cards to keep the style, font, colors etc consistent.

-I would like to include my slogan
Care That Comes To You

-I would like it to include services options with tick boxes for Mobile, Clinic, Telehealth, NPKRTW

-I would like for it to say Call to Book or Book Online

-I would like it to include my clinic address:
742 Larkin Crescent
Whitehorse, YT
Y1B2K9

-I would like it to include my contact info:
Gavin Trusk BKin, MScPT, CGIMS, FCAMPT
(867)555-0142
physio@trusktherapy.ca

-I would like lines for the following:
Patient Name:
Diagnosis/Recommendations:
(extra lines to fill out patient info)

Physician Signature
Date

Target Market(s)

Physicians to refer clients to physiotherapy

Industry/Entity Type

Physical Therapy

Requirements
Must have
• Clean, concise, easy to look at and find pertinant categories for physicians
Nice to have
• Trusk Therapy color scheme. Please see business cards and website as needed
Should not have
• Not too cluttered or wordy

```html
<!DOCTYPE html>
<html lang="en">
<head>
<meta charset="utf-8">
<title>Physiotherapy Referral – Trusk Therapy</title>
<link rel="stylesheet" href="https://fonts.googleapis.com/css2?family=Roboto+Slab:wght@700&family=Noticia+Text:ital,wght@0,700;1,700&family=Tinos:wght@400;700&display=swap">
<style>
  :root {
    --navy: #2c4870;
    --green: #155a4a;
    --rule-grey: #d3d4d6;
    --slogan-grey: #b5b6b8;
    --ink: #1a1a1a;
    --paper: #ffffff;
  }
  * { box-sizing: border-box; margin: 0; padding: 0; }
  html, body { width: 845px; height: 1200px; overflow: hidden; background: var(--paper); }
  .pad { position: relative; width: 845px; height: 1200px; overflow: hidden; font-family: "Tinos", "Times New Roman", serif; color: var(--ink); }
  .abs { position: absolute; }

  .brand { left: 58px; top: 108px; display: flex; align-items: center; gap: 12px; }
  .brand-mark { width: 22px; height: 22px; background: var(--navy); }
  .brand-name { font-family: "Roboto Slab", Georgia, serif; font-weight: 700; font-size: 34px; color: var(--navy); line-height: 1; }

  .practitioner { left: 550px; top: 60px; white-space: nowrap; }
  .practitioner-name { font-family: "Roboto Slab", Georgia, serif; font-weight: 700; font-size: 23px; color: var(--navy); line-height: 1.1; }
  .credentials { font-size: 17px; color: var(--green); margin-top: 8px; }
  .practice { left: 551px; top: 152px; white-space: nowrap; font-family: "Noticia Text", Georgia, serif; font-style: italic; font-weight: 700; font-size: 25px; color: var(--navy); }
  .slogan { left: 551px; top: 189px; white-space: nowrap; font-family: "Noticia Text", Georgia, serif; font-style: italic; font-weight: 700; font-size: 17px; color: var(--slogan-grey); }

  .header-rule { left: 51px; top: 237px; width: 743px; height: 2px; background: var(--rule-grey); }
  .title-tab { left: 216px; top: 237px; width: 412px; height: 36px; background: var(--rule-grey); clip-path: polygon(0 0, 100% 0, 92.2% 100%, 7.8% 100%); }
  .title { left: 216px; top: 241px; width: 412px; text-align: center; font-family: "Noticia Text", Georgia, serif; font-weight: 700; font-variant: small-caps; font-size: 25px; color: var(--navy); letter-spacing: 0.3px; }

  .field { display: flex; align-items: baseline; font-size: 22.5px; }
  .field .fill { flex: 1; margin-left: 6px; border-bottom: 1.6px dotted #333; height: 1px; }
  .line { left: 83px; width: 682px; border-bottom: 1.6px dotted #333; }

  .services-label { left: 77px; top: 767px; font-size: 22.5px; }
  .options { left: 77px; top: 809px; font-size: 24px; }
  .option { position: absolute; display: flex; align-items: center; gap: 8px; white-space: nowrap; }
  .box { width: 24px; height: 24px; border: 1.4px solid #222; background: var(--paper); }

  .footer { left: 0; top: 1043px; width: 845px; height: 157px; background: var(--navy); color: #fff; }
  .footer-name { left: 77px; top: 20px; font-family: "Roboto Slab", Georgia, serif; font-weight: 700; font-size: 22px; }
  .address { left: 77px; top: 56px; font-size: 20px; line-height: 27px; }
  .cta { left: 535px; top: 20px; white-space: nowrap; font-family: "Noticia Text", Georgia, serif; font-style: italic; font-weight: 700; font-size: 20px; }
  .contacts { left: 538px; top: 56px; font-size: 20px; line-height: 27px; }
  .contact { display: flex; align-items: center; gap: 14px; }
  .contact svg { width: 14px; height: 14px; flex: none; }
</style>
</head>
<body>
<main class="pad">
  <div class="abs brand"><span class="brand-mark"></span><span class="brand-name">Trusk Therapy</span></div>

  <div class="abs practitioner">
    <div class="practitioner-name">Gavin Trusk</div>
    <div class="credentials">BKin, MScPT, CGIMS, FCAMPT</div>
  </div>
  <div class="abs practice">Boreal Rehab Clinic</div>
  <div class="abs slogan">Care That Comes To You</div>

  <div class="abs header-rule"></div>
  <div class="abs title-tab"></div>
  <h1 class="abs title">Physiotherapy Referral</h1>

  <div class="abs field" style="left:77px; top:334px; width:688px;"><span>Patient Name :</span><span class="fill"></span></div>
  <div class="abs field" style="left:77px; top:388px; width:690px;"><span>Diagnosis/Recommendations :</span><span class="fill"></span></div>
  <div class="abs line" style="top:462px;"></div>
  <div class="abs line" style="top:516px;"></div>
  <div class="abs line" style="top:570px;"></div>
  <div class="abs line" style="top:624px;"></div>
  <div class="abs line" style="top:678px;"></div>
  <div class="abs line" style="top:732px;"></div>

  <div class="abs services-label">Services :</div>
  <div class="abs options">
    <label class="option" style="left:0;"><span class="box"></span>Mobile</label>
    <label class="option" style="left:160px;"><span class="box"></span>Clinic</label>
    <label class="option" style="left:313px;"><span class="box"></span>Telehealth</label>
    <label class="option" style="left:505px;"><span class="box"></span>NPKRTW</label>
  </div>

  <div class="abs field" style="left:77px; top:918px; width:482px;"><span>Physician Signature :</span><span class="fill"></span></div>
  <div class="abs field" style="left:77px; top:972px; width:240px;"><span>Date :</span><span class="fill"></span></div>

  <footer class="abs footer">
    <div class="abs footer-name">Trusk Therapy</div>
    <div class="abs address">742 Larkin Crescent<br>Whitehorse, YT<br>Y1B2K9</div>
    <div class="abs cta">Call to Book or Book Online</div>
    <div class="abs contacts">
      <div class="contact"><svg viewBox="0 0 16 16" aria-hidden="true"><path fill="#fff" d="M3.5 1.5l2.5 0 1 3.5-1.8 1.2a8 8 0 0 0 4.6 4.6l1.2-1.8 3.5 1v2.5c0 .8-.7 1.5-1.5 1.5C7 14 2 9 2 3c0-.8.7-1.5 1.5-1.5z"/></svg><span>(867)555-0142</span></div>
      <div class="contact"><svg viewBox="0 0 16 16" aria-hidden="true"><rect x="1.5" y="3.5" width="13" height="9" fill="none" stroke="#fff" stroke-width="1.4"/><path d="M1.5 3.5 8 9l6.5-5.5" fill="none" stroke="#fff" stroke-width="1.4"/></svg><span>physio@trusktherapy.ca</span></div>
      <div class="contact"><svg viewBox="0 0 16 16" aria-hidden="true"><g fill="none" stroke="#fff" stroke-width="1.2"><circle cx="8" cy="8" r="6.5"/><ellipse cx="8" cy="8" rx="3" ry="6.5"/><path d="M1.5 8h13M2.5 4.8h11M2.5 11.2h11"/></g></svg><span>www.trusktherapy.ca</span></div>
    </div>
  </footer>
</main>
</body>
</html>
```